BRIGHTDESK COWORKING Website design and coding

BRIGHTDESK COWORKING

BRIGHTDESK is Galveston’s first (and currently only) shared business co-working space. We share the same upscale, casual work environment, but we work independently on our own (or our team’s) projects and goals. For only a flat $195 membership fee per month, you have your very own all-inclusive, fun, personal business office environment. Website is written (Word file #12, below); and all pictures etc provided. Galveston is a beachy, coastal, historic city an hour from Houston, Texas USA. Logo (file 11 below) is temporary only.

Target Market(s)

Outside sales people, medical students looking for study hall, Houston companies looking for local office, real estate agents, graphic artists, entrepreneurs, etc

Contact Information for Business Card

will discuss --want to combine with current business card with multiple businesses

Logo Text

BRIGHTDESK COWORKING

Coding

Coded - Design and coding required

Number of Pages Required

5+ page

Colors
ec1f27
fbed22

Requirements
Nice to have
• maroon/wine dominant with yellow and red accents, gray base are the colors of the space--website could coordinate--but open to creative ideas/combinations

```html
<!DOCTYPE html>
<html lang="en">
<head>
<meta charset="utf-8">
<title>BRIGHTDESK COWORKING</title>
<link rel="stylesheet" href="https://fonts.googleapis.com/css2?family=Crimson+Pro:wght@500;600&family=Poppins:wght@300;400;500&family=Raleway:wght@300;500&family=Oswald:wght@500;600&display=swap">
<style>
:root{
  --maroon:#8c0a0a;
  --wine:#7a0b0b;
  --red:#a10f12;
  --yellow:#f9ec22;
  --gray:#f3f3f3;
  --ink:#333;
  --muted:#666;
  --black:#0a0a0a;
  --white:#fff;
}
*{margin:0;padding:0;box-sizing:border-box}
html,body{width:1200px;height:4084px;overflow:hidden}
body{position:relative;background:var(--white);font-family:"Poppins",sans-serif;color:var(--ink);font-weight:300}
.abs{position:absolute}
.serif{font-family:"Crimson Pro",serif;font-weight:600;color:var(--maroon)}
.btn{position:absolute;background:var(--maroon);color:#fff;font-family:"Crimson Pro",serif;font-weight:500;font-size:16px;letter-spacing:.5px;display:flex;align-items:center;justify-content:center}
.photo{position:absolute}

/* top bar & nav */
.topbar{left:0;top:0;width:1200px;height:34px;background:var(--maroon)}
.topbar .contact{position:absolute;top:0;height:34px;display:flex;align-items:center;gap:10px;color:#fff;font-size:12px}
.ring{width:24px;height:24px;border-radius:50%;border:2px solid var(--yellow);display:flex;align-items:center;justify-content:center}
.social-dot{position:absolute;width:24px;height:24px;border-radius:50%;background:var(--yellow)}
.nav{left:0;top:34px;width:1200px;height:64px;background:#fff;box-shadow:0 1px 4px rgba(0,0,0,.08)}
.logo-box{left:60px;top:20px;width:180px;height:86px;background:#fff;box-shadow:0 2px 8px rgba(0,0,0,.15);display:flex;flex-direction:column;align-items:center;justify-content:center;z-index:3}
.logo-box .name{font-family:"Crimson Pro",serif;font-weight:600;color:var(--maroon);font-size:26px;line-height:1}
.logo-box .sub{font-family:"Crimson Pro",serif;font-weight:600;color:var(--maroon);font-size:15px;letter-spacing:2px}
.menu{position:absolute;left:392px;top:0;height:64px;display:flex;align-items:center;gap:22px;font-size:11px;color:#333;font-weight:400}
.menu .active{color:var(--maroon);border-bottom:2px solid var(--maroon);padding-bottom:3px}
.quote{left:1001px;top:48px;width:139px;height:36px;font-size:15px}

/* hero */
.hero{left:0;top:98px;width:1200px;height:614px;background:linear-gradient(135deg,#3b3630 0%,#5a564c 45%,#2c2a26 75%,#6b5e2a 100%)}
.hero-title{left:62px;top:322px;font-family:"Raleway",sans-serif;color:#fff;font-size:48px;line-height:54px;font-weight:300}
.hero-title b{font-weight:500}

/* intro row */
.intro-photo{left:0;top:712px;width:338px;height:293px;background:linear-gradient(160deg,#c9b9a4,#8a7260 60%,#e8e2da)}
.intro-offer{left:338px;top:712px;width:247px;height:293px;background:var(--yellow);display:flex;flex-direction:column;align-items:center;justify-content:center;font-family:"Oswald",sans-serif;font-weight:600;color:var(--maroon);text-align:center;line-height:1.5;letter-spacing:-.3px}
.intro-offer .l1{font-size:22px}
.intro-offer .price{font-size:34px;margin:2px 0 6px}
.intro-offer .l2{font-size:22px}
.intro-text{left:585px;top:712px;width:615px;height:293px;background:var(--gray)}
.intro-text h2{position:absolute;left:66px;top:62px;font-size:31px;letter-spacing:.5px}
.intro-text p{position:absolute;left:66px;width:450px;font-size:11.5px;line-height:21px;color:var(--muted)}

/* amenities */
.why{left:214px;top:1080px;font-size:14px;font-weight:400;color:#222}
.amen-title{left:211px;top:1100px;font-size:32px}
.amen-lead{left:211px;top:1152px;width:360px;font-size:11.5px;line-height:20px;color:var(--muted)}
.amen-list{left:211px;top:1230px;width:350px;list-style:none;font-size:11.5px;line-height:19px;color:#444}
.amen-list li{position:relative;padding-left:26px;margin-bottom:10px}
.amen-list li::before{content:"";position:absolute;left:2px;top:5px;width:8px;height:8px;background:var(--maroon);transform:rotate(45deg);box-shadow:2px 2px 0 var(--yellow)}
.explore-1{left:211px;top:1442px;width:139px;height:36px}
.amen-stripes{left:741px;top:1160px;width:310px;height:302px}
.amen-black{left:695px;top:1205px;width:275px;height:280px;background:var(--black)}
.amen-yellow{left:675px;top:1432px;width:65px;height:68px;background:var(--yellow);border-top-right-radius:40px}
.amen-photo{left:720px;top:1089px;width:315px;height:362px;background:linear-gradient(180deg,#d8c79a,#b58a45 55%,#5e3d1f)}

/* membership */
.member{left:0;top:1577px;width:1200px;height:413px;background:linear-gradient(100deg,var(--red),#8a0a0c 60%,#9c0e10)}
.member-yellow{left:525px;top:1961px;width:675px;height:54px;background:var(--yellow)}
.member h2{position:absolute;left:206px;top:70px;font-size:30px;color:#fff;font-family:"Crimson Pro",serif;font-weight:500}
.member p{position:absolute;left:206px;width:370px;font-size:11.5px;line-height:19px;color:#fff}
.member .cta{position:absolute;left:206px;top:267px;font-size:16px;line-height:22px;color:var(--yellow);font-weight:400}
.member .cta span{font-family:"Crimson Pro",serif;text-decoration:underline;font-weight:600}
.member-person{left:700px;top:1625px;width:330px;height:375px;background:radial-gradient(ellipse at 50% 45%,#f2b733 0%,#d99a26 35%,#5d7fa8 70%,rgba(93,127,168,0) 72%)}

/* pictures */
.pic-title{left:0;top:2086px;width:1200px;text-align:center;font-size:32px}
.pic-sub{left:0;top:2132px;width:1200px;text-align:center;font-size:13px;color:#333;font-weight:400}
.tile{position:absolute;width:247px;height:193px}
.explore-2{left:531px;top:2614px;width:138px;height:36px}

/* philosophy */
.phil-band{left:0;top:2958px;width:1200px;height:418px;background:var(--gray)}
.phil-title{left:133px;top:2760px;font-size:32px;line-height:38px}
.phil-photo{left:135px;top:2867px;width:502px;height:324px;background:linear-gradient(180deg,#6b6a62 0%,#8e8a7f 45%,#d8b267 75%,#e7c989 100%)}
.phil-item{position:absolute;left:707px;width:440px}
.phil-icon{position:absolute;left:0;top:0;width:60px;height:60px;border-radius:50%;background:var(--yellow);display:flex;align-items:center;justify-content:center}
.phil-item h3{position:absolute;left:83px;top:0;font-family:"Crimson Pro",serif;font-weight:600;color:var(--maroon);font-size:15.5px;letter-spacing:.3px;white-space:nowrap}
.phil-item p{position:absolute;left:85px;top:24px;width:320px;font-size:11px;line-height:20px;color:var(--muted)}
.phil-item .more{position:absolute;left:86px;top:72px;font-family:"Crimson Pro",serif;font-size:13px;color:var(--maroon);text-decoration:underline;display:flex;align-items:center;gap:6px}
.phil-item .more i{width:13px;height:13px;border:1px solid var(--yellow);border-radius:50%;display:inline-block}

/* social tags */
.tag-title{left:0;top:3446px;width:1200px;text-align:center;font-size:32px;text-decoration:underline}
.tag{position:absolute;top:3528px;width:151px;height:113px}
.follow{left:0;top:3672px;width:1200px;text-align:center;font-family:"Crimson Pro",serif;color:var(--yellow);font-size:15px;text-decoration:underline}

/* footer */
.footer{left:0;top:3765px;width:1200px;height:319px;background:var(--black);color:#ddd}
.footer h4{position:absolute;top:45px;font-family:"Crimson Pro",serif;font-weight:500;font-size:15px;color:#fff;letter-spacing:.3px}
.footer .txt{position:absolute;font-size:11.5px;line-height:21px;color:#ccc}
.footer .ico{position:absolute}
.f-logo{position:absolute;left:60px;top:42px;font-family:"Crimson Pro",serif;font-weight:600;color:var(--red);font-size:28px;line-height:1}
.f-logo-sub{position:absolute;left:80px;top:74px;font-family:"Crimson Pro",serif;font-weight:600;color:#fff;font-size:16px;letter-spacing:2px}
.f-social{position:absolute;top:212px;width:28px;height:28px}
.email-box{position:absolute;left:934px;top:110px;width:206px;height:36px;background:#1c1c1c;border:1px solid #333;font-size:11px;color:#ccc;display:flex;align-items:center;padding-left:12px}
.subscribe{left:937px;top:156px;width:121px;height:36px;font-size:15px}
.copy{position:absolute;left:0;top:290px;width:1200px;text-align:center;font-size:11px;color:#aaa}
.copy span{color:var(--red)}
</style>
</head>
<body>

<div class="abs topbar">
  <div class="contact" style="left:705px">
    <span class="ring"><svg width="12" height="12" viewBox="0 0 24 24"><path fill="#f9ec22" d="M6.6 10.8a15 15 0 006.6 6.6l2.2-2.2c.3-.3.7-.4 1-.2 1.1.4 2.3.6 3.6.6.6 0 1 .4 1 1V20c0 .6-.4 1-1 1A17 17 0 013 4c0-.6.4-1 1-1h3.5c.6 0 1 .4 1 1 0 1.3.2 2.5.6 3.6.1.3 0 .7-.2 1z"/></svg></span>
    <span>hello@harborleasepartners.com</span>
  </div>
  <div class="contact" style="left:908px">
    <span class="ring"><svg width="12" height="10" viewBox="0 0 24 18"><rect x="1" y="1" width="22" height="16" fill="none" stroke="#f9ec22" stroke-width="2"/><path d="M1 1l11 9 11-9" fill="none" stroke="#f9ec22" stroke-width="2"/></svg></span>
    <span>555-014-2290</span>
  </div>
  <div class="social-dot" style="left:1051px;top:5px"></div>
  <div class="social-dot" style="left:1081px;top:5px"></div>
  <div class="social-dot" style="left:1111px;top:5px"></div>
</div>

<div class="abs nav">
  <div class="menu">
    <span class="active">HOME</span><span>ABOUT</span><span>AMENITIES</span><span>MEMBERSHIP</span><span>PICTURES</span><span>THE BRIGHTDESK PHILOSOPHY</span><span>CONTACT</span>
  </div>
</div>
<div class="abs logo-box"><span class="name">BrightDesk</span><span class="sub">COWORKING</span></div>
<div class="btn quote">GET A QUOTE</div>

<div class="photo hero" role="img" aria-label="Coworking lounge with sofas, lockers and yellow-and-black desk chairs"></div>
<div class="abs hero-title">World's 1st Private<br><b>Coworking Space</b></div>

<div class="photo intro-photo" role="img" aria-label="Team of women working together around a laptop"></div>
<div class="abs intro-offer">
  <span class="l1">FOR ONLY A FLAT</span>
  <span class="price">$195</span>
  <span class="l2">MEMBERSHIP FEE</span>
  <span class="l2">PER MONTH</span>
</div>
<div class="abs intro-text">
  <h2 class="serif">BRIGHTDESK COWORKING</h2>
  <p style="top:112px">BRIGHTDESK is Galveston's first (and currently only) shared business co-working space. We share the same upscale, casual work environment, but we work independently on our own (or our team's) projects and goals.</p>
  <p style="top:186px">For only a flat $195 membership fee per month, you have your very own all-inclusive, fun, personal business office environment.</p>
</div>

<div class="abs why">WHY US ?</div>
<div class="abs serif amen-title">AMENITIES</div>
<p class="abs amen-lead">BRIGHTDESK is the first Galveston co-working space, and offers all of the following features, all included in your monthly $195 membership fee:</p>
<ul class="abs amen-list">
  <li>Open office or a private cubicle for your daily use.</li>
  <li>Free Wifi</li>
  <li>Comfortable open casual spaces or private office cubicles – at your option</li>
  <li>Keyless, digital door entry</li>
  <li>Great location – a block from the Lantern Row area of coffee bars, restaurants, bars, art galleries, and the old Bayview Playhouse</li>
</ul>
<div class="btn explore-1">EXPLORE ALL</div>

<svg class="abs amen-stripes" viewBox="0 0 310 302" aria-hidden="true">
  <defs><pattern id="hatch" width="7" height="7" patternUnits="userSpaceOnUse" patternTransform="rotate(45)"><rect width="3" height="7" fill="#bbb"/></pattern></defs>
  <rect x="295" y="0" width="15" height="302" fill="url(#hatch)"/>
  <rect x="0" y="287" width="310" height="15" fill="url(#hatch)"/>
</svg>
<div class="abs amen-black"></div>
<div class="abs amen-yellow"></div>
<div class="photo amen-photo" role="img" aria-label="Meeting room with long wooden table, benches and pendant lamps"></div>

<div class="abs member-yellow"></div>
<div class="abs member">
  <h2>MEMBERSHIP</h2>
  <p style="top:120px">For only $195 a month, charged to your credit card, you get the all-inclusive amenities listed above, for one flat fee. The only "extras" are for copies, on a per-copy basis.</p>
  <p style="top:191px">WiFi, coffee, use of the conference room, office use, use of the kitchen and all the other features listed under "AMENITIES" above, are "INCLUDED" at no additional cost.</p>
  <div class="cta">Get A FREE Day, To Try Us Out By<br>Emailing Us At The <span>Link Here</span></div>
</div>
<div class="photo member-person" role="img" aria-label="Smiling woman sitting cross-legged with a laptop"></div>

<div class="abs serif pic-title">PICTURE</div>
<div class="abs pic-sub">For Only A Flat $195 Membership Fee Per Month</div>
<div class="tile" style="left:206px;top:2183px;background:linear-gradient(135deg,#f3e64a,#e6d733)" role="img" aria-label="Office interior under yellow overlay"></div>
<svg class="abs" style="left:206px;top:2183px" width="247" height="193" aria-hidden="true"><rect x="10" y="10" width="227" height="173" fill="none" stroke="#8c0a0a" stroke-width="1"/><path d="M123.5 78v38M104.5 97h38" stroke="#8c0a0a" stroke-width="1.5"/></svg>
<div class="tile" style="left:476px;top:2183px;background:linear-gradient(160deg,#c9c9c2,#5a4a44 55%,#1c1c1c)" role="img" aria-label="Lounge with black leather sofas and lockers"></div>
<div class="tile" style="left:746px;top:2183px;background:linear-gradient(160deg,#e9e4da,#bfae8c 55%,#55504a)" role="img" aria-label="Open workspace with white sofa and desks"></div>
<div class="tile" style="left:206px;top:2400px;background:linear-gradient(160deg,#d8d6cf,#8d7a6a 55%,#3b2a22)" role="img" aria-label="Kitchen with bar stools and refrigerator"></div>
<div class="tile" style="left:476px;top:2400px;background:linear-gradient(160deg,#6c5a3c,#d79b3a 55%,#f2c35c)" role="img" aria-label="Conference room with long yellow table"></div>
<div class="tile" style="left:746px;top:2400px;background:linear-gradient(160deg,#2b2a2c,#4d4f5a 45%,#e3b840)" role="img" aria-label="Desk area with yellow tables and pendant lamps"></div>
<div class="btn explore-2">EXPLORE ALL</div>

<div class="abs phil-band"></div>
<div class="abs serif phil-title">THE BRIGHTDESK<br>PHILOSOPHY</div>
<div class="photo phil-photo" role="img" aria-label="Kitchen counter with a pink vase holding a green plant"></div>

<div class="phil-item" style="top:2818px">
  <div class="phil-icon"><svg width="28" height="28" viewBox="0 0 24 24"><circle cx="12" cy="5" r="2.5" fill="#8c0a0a"/><path d="M12 9v6h5l2 5" fill="none" stroke="#8c0a0a" stroke-width="2"/><path d="M9 11a6 6 0 108 8" fill="none" stroke="#8c0a0a" stroke-width="2"/></svg></div>
  <h3>WORK OUTSIDE THE HOME</h3>
  <p>Free yourself for the burdens of house or school, and work in anenvironment that MOTIVATES you instead....</p>
  <span class="more">Learn More <i></i></span>
</div>
<div class="phil-item" style="top:2959px">
  <div class="phil-icon"><svg width="28" height="28" viewBox="0 0 24 24"><path d="M4 14l6-6 3 3 4-4 3 3-7 8z" fill="#8c0a0a"/></svg></div>
  <h3>BRIGHTDESK THE COMPETITION</h3>
  <p>Because of the flexibility, prestigious location, opportunities to meet and network with active....</p>
  <span class="more">Learn More <i></i></span>
</div>
<div class="phil-item" style="top:3084px">
  <div class="phil-icon"><svg width="28" height="28" viewBox="0 0 24 24"><circle cx="8" cy="5" r="2.3" fill="#8c0a0a"/><circle cx="16" cy="5" r="2.3" fill="#8c0a0a"/><path d="M5 9h6v6H9v6H7v-6H5zM13 9h6v6h-2v6h-2v-6h-2z" fill="#8c0a0a"/></svg></div>
  <h3>WORK IT OUT WITH YOUR COWORKERS.</h3>
  <p>BRIGHTDESK is a community – if you are making a pot of (free) coffee – ask and make enough for everyone...</p>
  <span class="more">Learn More <i></i></span>
</div>
<div class="phil-item" style="top:3219px">
  <div class="phil-icon"><svg width="28" height="28" viewBox="0 0 24 24"><circle cx="10" cy="4" r="2.3" fill="#8c0a0a"/><path d="M8 8h4l2 6h5v2h-6l-2-4v9H9z" fill="#8c0a0a"/><rect x="4" y="19" width="15" height="2" fill="#8c0a0a"/></svg></div>
  <h3>WORK OUT THE PATH TO YOUR SUCCESS</h3>
  <p>As your business grows, there are other beautiful, "dedicated desk" private executive offices, and....</p>
  <span class="more">Learn More <i></i></span>
</div>

<div class="abs serif tag-title">#BrightdeskCoworking</div>
<div class="tag" style="left:179px;background:#f4e42a" role="img" aria-label="Social post graphic: Work out the path to success"></div>
<div class="tag" style="left:352px;background:#d8131b" role="img" aria-label="Social post graphic: Work it out with your coworkers"></div>
<div class="tag" style="left:525px;background:linear-gradient(135deg,#9a1a2a,#5a0a12)" role="img" aria-label="Social post graphic: Work outside the home"></div>
<div class="tag" style="left:697px;background:#a3101c" role="img" aria-label="Social post graphic: BrightDesk Coworking"></div>
<div class="tag" style="left:870px;background:#f6e61c" role="img" aria-label="Social post graphic: Outdo the competition"></div>
<div class="abs follow">Follow Us</div>

<div class="abs footer">
  <div class="f-logo">BrightDesk</div>
  <div class="f-logo-sub">COWORKING</div>

  <svg class="ico" style="left:60px;top:125px" width="16" height="12" viewBox="0 0 24 18"><rect x="1" y="1" width="22" height="16" fill="none" stroke="#f9ec22" stroke-width="2"/><path d="M1 1l11 9 11-9" fill="none" stroke="#f9ec22" stroke-width="2"/></svg>
  <div class="txt" style="left:89px;top:117px;width:150px">brightdeskcowork@mail<br>box.com</div>
  <svg class="ico" style="left:60px;top:172px" width="14" height="14" viewBox="0 0 24 24"><path fill="#f9ec22" d="M6.6 10.8a15 15 0 006.6 6.6l2.2-2.2c.3-.3.7-.4 1-.2 1.1.4 2.3.6 3.6.6.6 0 1 .4 1 1V20c0 .6-.4 1-1 1A17 17 0 013 4c0-.6.4-1 1-1h3.5c.6 0 1 .4 1 1 0 1.3.2 2.5.6 3.6.1.3 0 .7-.2 1z"/></svg>
  <div class="txt" style="left:89px;top:168px">555-014-2290</div>
  <div class="f-social" style="left:60px;border:1.5px solid #f9ec22"></div>
  <div class="f-social" style="left:96px;background:#a10f12"></div>
  <div class="f-social" style="left:132px;background:#a10f12"></div>

  <h4 style="left:271px">PHYSICAL LOCATION</h4>
  <svg class="ico" style="left:271px;top:100px" width="14" height="18" viewBox="0 0 24 30"><path d="M12 1a10 10 0 00-10 10c0 8 10 18 10 18s10-10 10-18A10 10 0 0012 1z" fill="none" stroke="#f9ec22" stroke-width="2.5"/><circle cx="12" cy="11" r="3.5" fill="#f9ec22"/></svg>
  <div class="txt" style="left:297px;top:96px;width:160px">BrightDesk Coworking 418 Seawall Row, Suite 12 Galveston, TX 77550</div>

  <h4 style="left:488px">OWNER</h4>
  <svg class="ico" style="left:488px;top:104px" width="16" height="12" viewBox="0 0 24 18"><rect x="1" y="1" width="22" height="16" fill="none" stroke="#f9ec22" stroke-width="2"/><path d="M1 1l11 9 11-9" fill="none" stroke="#f9ec22" stroke-width="2"/></svg>
  <div class="txt" style="left:519px;top:96px">Harbor Lease Partners<br>hello@harborleasepartners.com</div>
  <svg class="ico" style="left:488px;top:150px" width="14" height="14" viewBox="0 0 24 24"><path fill="#f9ec22" d="M6.6 10.8a15 15 0 006.6 6.6l2.2-2.2c.3-.3.7-.4 1-.2 1.1.4 2.3.6 3.6.6.6 0 1 .4 1 1V20c0 .6-.4 1-1 1A17 17 0 013 4c0-.6.4-1 1-1h3.5c.6 0 1 .4 1 1 0 1.3.2 2.5.6 3.6.1.3 0 .7-.2 1z"/></svg>
  <div class="txt" style="left:519px;top:146px">555-014-2290</div>

  <h4 style="left:715px">MAILING LIST</h4>
  <svg class="ico" style="left:715px;top:100px" width="14" height="18" viewBox="0 0 24 30"><path d="M12 1a10 10 0 00-10 10c0 8 10 18 10 18s10-10 10-18A10 10 0 0012 1z" fill="none" stroke="#f9ec22" stroke-width="2.5"/><circle cx="12" cy="11" r="3.5" fill="#f9ec22"/></svg>
  <div class="txt" style="left:743px;top:96px;width:150px">Harbor Lease Partners 95 Bayou Lane, Suite 40 Houston, TX 77002</div>

  <h4 style="left:932px">NEWSLETTER SIGNUP!</h4>
  <div class="txt" style="left:934px;top:84px;width:200px">Would you like to receive our exclusive update for signup!</div>
  <div class="email-box">Enter Email *
    <svg style="position:absolute;right:10px;top:13px" width="12" height="9" viewBox="0 0 24 18"><rect x="1" y="1" width="22" height="16" fill="none" stroke="#f9ec22" stroke-width="2"/><path d="M1 1l11 9 11-9" fill="none" stroke="#f9ec22" stroke-width="2"/></svg>
  </div>
  <div class="btn subscribe">SUBSCRIBE</div>

  <div class="copy">©<span>BrightDesk</span> -2020 All rights reserved.</div>
</div>

</body>
</html>
```